Stylish Business Card for Modern hair salon

I need a simple business card design using our salon logo and colours that are in the logo. We service clients of all ages but predominantly those in the 18 to 55 age range. We have a young staff and are looking to have a card that will present a modern and clean image that represents who we are. The card should be in black and white same as our logo. Minimal use of other colours is allowed.

Industry/Entity Type

Hair And Beauty

Contact Information for Business Card

The design should have the following information
salon name - TR Hair Studio
address - 2751 Birchfield Rd.E. Mississauga, ON L7P3K2
phone - 905 614-2870
website - trhairexample.ca
instagram - tr.hairstudio
twitter - @TR_HairStudio

Colors
000000
ffffff
474747

Requirements
Must have
• simple design, salon name, address, phone, website, instagram, twitter info
• Back of card should have the following:
• YOUR NEXT APPOINTMENT
• DATE
• TIME
Nice to have
• simple design, clear to see and read,
• predominantly black and white colour, minimal use of other colours is ok
Should not have
• many colours, various fonts

```html
<!DOCTYPE html>
<html lang="en">
<head>
<meta charset="utf-8">
<title>TR Hair Studio – Business Card</title>
<link href="https://fonts.googleapis.com/css2?family=Poppins:wght@400;500&display=swap" rel="stylesheet">
<style>
  :root {
    --black: #1a1a1a;
    --ink: #474747;
    --white: #ffffff;
    --silver: #e4e4e4;
    --backdrop: #ebebeb;
  }
  * { margin: 0; padding: 0; box-sizing: border-box; }
  html, body { width: 1200px; height: 747px; overflow: hidden; }
  body {
    background: var(--backdrop);
    font-family: "Poppins", sans-serif;
    color: var(--ink);
    position: relative;
  }
  .card {
    position: absolute;
    top: 225px;
    width: 520px;
    height: 297px;
    box-shadow: 0 10px 28px rgba(0,0,0,0.14);
  }
  .card--front {
    left: 50px;
    background: var(--black);
    display: flex;
    align-items: center;
    justify-content: center;
  }
  .front-name {
    color: var(--silver);
    font-size: 40px;
    font-weight: 400;
    letter-spacing: 1px;
  }
  .card--back {
    left: 630px;
    background: var(--white);
  }
  .back-name {
    position: absolute;
    left: 40px;
    top: 70px;
    width: 180px;
    text-align: center;
    font-size: 24px;
    font-weight: 400;
    color: var(--ink);
  }
  .appointment {
    position: absolute;
    left: 40px;
    top: 188px;
    width: 200px;
  }
  .appointment-title {
    font-size: 11.5px;
    font-weight: 500;
    letter-spacing: 0.3px;
    margin-bottom: 5px;
    color: var(--ink);
  }
  .appointment-box {
    border: 1px solid var(--ink);
  }
  .appointment-row {
    height: 37px;
    padding: 8px 6px;
    font-size: 12px;
  }
  .appointment-row + .appointment-row { border-top: 1px solid var(--ink); }
  .contact {
    position: absolute;
    left: 285px;
    top: 68px;
  }
  .contact-name { font-size: 16px; font-weight: 500; line-height: 1.3; }
  .contact-address { font-size: 15px; line-height: 1.35; }
  .contact-list { list-style: none; margin-top: 18px; }
  .contact-list li {
    display: flex;
    align-items: center;
    gap: 10px;
    font-size: 15px;
    line-height: 26px;
  }
  .contact-icon { width: 14px; height: 14px; flex: none; }
</style>
</head>
<body>
  <section class="card card--front">
    <span class="front-name">TR Hair Studio</span>
  </section>

  <section class="card card--back">
    <div class="back-name">TR Hair Studio</div>

    <div class="appointment">
      <p class="appointment-title">YOUR NEXT APPOINTMENT</p>
      <div class="appointment-box">
        <div class="appointment-row">Date:</div>
        <div class="appointment-row">Time:</div>
      </div>
    </div>

    <div class="contact">
      <p class="contact-name">TR Hair Studio</p>
      <p class="contact-address">2751 Birchfield Rd.E.<br>Mississauga, ON L7P3K2</p>
      <ul class="contact-list">
        <li>
          <svg class="contact-icon" viewBox="0 0 14 14" aria-hidden="true"><path d="M1 4c0-2 2-3 6-3s6 1 6 3v1H10V3.5H4V5H1z M3 6h8l1.5 6.5h-11z" fill="#474747"/><circle cx="7" cy="9" r="1.6" fill="#fff"/></svg>
          905 614-2870
        </li>
        <li>
          <svg class="contact-icon" viewBox="0 0 14 14" aria-hidden="true"><g fill="none" stroke="#474747" stroke-width="1.2"><circle cx="7" cy="7" r="6"/><ellipse cx="7" cy="7" rx="2.6" ry="6"/><path d="M1 7h12M2 4h10M2 10h10"/></g></svg>
          trhairexample.ca
        </li>
        <li>
          <svg class="contact-icon" viewBox="0 0 14 14" aria-hidden="true"><rect x="1" y="1" width="12" height="12" fill="#474747"/></svg>
          tr.hairstudio
        </li>
        <li>
          <svg class="contact-icon" viewBox="0 0 14 14" aria-hidden="true"><circle cx="7" cy="7" r="6" fill="#474747"/></svg>
          @TR_HairStudio
        </li>
      </ul>
    </div>
  </section>
</body>
</html>
```